Flyer for Azienda Agricola Vendrano Wine producer

We need a flyer with the most important information about us. The structure of the flyer will be similar to the sample attached to this request.
We are a new producer of wine, In the Langhe region (Piemonte, Italy). We produce a small quantity of high quality wine. Our wines are Moscato d'Asti DOCG and Vermouth Bianco di Moscato d'Asti. From the next year we'll start to sell also 2 types of sparkling wine, one white and second rosè.
Our sales strategy is oriented to B2C thanks to our e-commerce web site and to other web opportunity (www.aziendaagricolavendrano.it).
In the attached file the labels of our wines, they can show the graphic still that we use since now, in particular we always use the leaf of grapes.
In case it can be usefull and in the flyer will be enough space, we can provide some others photo of ours grapes and panorama.
Thank in advance for your proposal
Marco

```html
<!DOCTYPE html>
<html lang="it">
<head>
<meta charset="utf-8">
<title>Azienda Agricola Vendrano – Flyer</title>
<link href="https://fonts.googleapis.com/css2?family=Cormorant+Garamond:wght@500&family=PT+Sans:ital,wght@0,400;0,700;1,400&family=PT+Sans+Narrow:wght@400;700&display=swap" rel="stylesheet">
<style>
:root{
  --bg:#d8d3cc;
  --sheet:#1f1f20;
  --sheet-2:#2a2a2b;
  --gold:#a88b2c;
  --gold-light:#c9a94a;
  --text:#d9d6d0;
  --muted:#a9a59d;
  --row-a:#3a3a3b;
  --row-b:#2c2c2d;
}
*{box-sizing:border-box;margin:0;padding:0}
html,body{width:1200px;height:911px;overflow:hidden;background:var(--bg)}
body{position:relative;font-family:"PT Sans",Arial,sans-serif;color:var(--text)}

.sheet{position:absolute;background:var(--sheet);overflow:hidden;box-shadow:0 3px 10px rgba(0,0,0,.25)}
.sheet-front{left:86px;top:72px;width:469px;height:714px}
.sheet-back{left:642px;top:126px;width:501px;height:714px}

/* front */
.brand-header{position:absolute;left:0;top:0;width:100%;height:90px;display:flex;align-items:center;justify-content:center;gap:10px}
.brand-name{font-family:"Cormorant Garamond",Georgia,serif;font-weight:500;font-size:52px;color:var(--gold);letter-spacing:1px}
.brand-dot{width:14px;height:14px;border-radius:50%;background:var(--gold)}
.vineyard-photo{position:absolute;left:0;top:90px;width:100%;height:280px;
  background:linear-gradient(180deg,#c9d6df 0%,#aab9a4 30%,#8c7a3c 55%,#b58a2a 75%,#6e5420 100%)}
.gold-rule{position:absolute;left:0;top:372px;width:100%;height:2px;background:var(--gold)}
.bottle-photo{position:absolute;left:310px;top:130px;width:146px;height:630px;border-radius:40px 40px 8px 8px;
  background:linear-gradient(90deg,#141414 0%,#3b3d30 35%,#55573f 50%,#2b2c24 70%,#111 100%)}
.front-copy{position:absolute;left:24px;top:388px;width:280px;font-size:7.6px;line-height:9.6px;text-align:justify}
.front-copy p{margin-bottom:8px}
.quote{font-style:italic}
.quote-source{font-style:italic;font-size:7px}
.web-band{position:absolute;left:0;bottom:0;width:100%;height:32px;background:var(--gold);
  display:flex;align-items:center;justify-content:center;font-size:14px;color:#111}

/* back */
.wine{position:absolute;left:0;width:100%}
.wine-moscato{top:24px}
.wine-vermouth{top:350px}
.wine-label{position:absolute;left:28px;top:0;width:116px;height:138px;border:1px solid #555;
  background:linear-gradient(160deg,#1a1a1a 0%,#2a2a2a 55%,#1c3a55 100%)}
.wine-title{position:absolute;left:157px;top:0;width:327px;height:26px;background:var(--gold);
  color:#fff;font-size:15px;line-height:26px;padding-left:8px}
.wine-text{position:absolute;left:157px;top:32px;width:327px;font-size:7.9px;line-height:9.6px;text-align:justify}
.tech{position:absolute;left:157px;width:236px;font-family:"PT Sans Narrow",Arial,sans-serif}
.wine-moscato .tech{top:198px}
.wine-vermouth .tech{top:124px}
.tech-title{font-size:6px;font-weight:700;text-transform:uppercase;margin-bottom:2px;color:var(--muted)}
.tech table{width:100%;border-collapse:collapse;font-size:5.2px}
.tech td{padding:0 3px;height:7px;line-height:7px}
.tech tr:nth-child(odd){background:var(--row-a)}
.tech tr:nth-child(even){background:var(--row-b)}
.tech td:first-child{width:64px;font-weight:700}

.back-footer{position:absolute;left:28px;top:600px;width:460px;height:66px}
.footer-brand{position:absolute;left:0;top:4px;display:flex;flex-direction:column;align-items:center}
.footer-brand .brand-name{font-size:34px;line-height:34px}
.footer-brand .brand-sub{font-size:10px;color:var(--gold);letter-spacing:.5px;text-transform:uppercase}
.contact{position:absolute;left:126px;top:0;font-size:7.4px;line-height:9.4px;color:var(--muted)}
.contact strong{color:var(--gold)}
</style>
</head>
<body>

<section class="sheet sheet-front">
  <header class="brand-header">
    <span class="brand-name">Vendrano</span>
    <span class="brand-dot"></span>
  </header>
  <div class="vineyard-photo" role="img" aria-label="Foto dei vigneti in collina in autunno con filari gialli e cielo"></div>
  <div class="gold-rule"></div>
  <div class="front-copy">
    <p class="quote">"Traversai Belbo, sulla passerella, e mentre andavo rimuginavo che non c'è niente di più bello di una vigna ben zappata, ben legata con le foglie giuste e quell'odore della terra cotta dal sole d'agosto. Una vigna ben lavorata è come un fisico sano, un corpo che vive, che ha il respiro e il suo sudore."</p>
    <p class="quote">"A Canelli entrai per un lungo viale che ai miei tempi non c'era, ma sentii subito l'odore, quella punta di vinaccia, di arietta di Belbo, di Vermuth."</p>
    <p class="quote-source">(Luigi Morando da Colline d'estate)</p>
    <p>L'Azienda Agricola Vendrano è sita sulla collina di Vendrano da cui prende il nome.<br>
    Il territorio in cui si trova è quello del Comune di Borgo Alto, oggi riconosciuto come patrimonio dell'Unesco per la bellezza del territorio e per la maestria dei piemontesi che hanno saputo fare la storia del vino e produrre alcuni dei migliori al mondo.<br>
    L'Azienda nasce dalla passione per la terra e per i suoi prodotti; con l'esperienza maturata in decenni produce i suoi vini partendo dalle migliori uve della sua terra.</p>
    <p>Il nome dell'etichetta, Cò Ciaro, nasce da come gli abitanti delle colline vicine chiamano la collina di Vendrano, perché, verso la fine dell'inverno guardando la collina di Vendrano si vede la cima ancora innevata mentre tutto intorno la primavera esplode; questa particolare caratteristica è data dall'esposizione a Nord Ovest della sua cima.</p>
  </div>
  <div class="bottle-photo" role="img" aria-label="Foto della bottiglia di Moscato d'Asti Cò Ciaro con etichetta scura"></div>
  <footer class="web-band">www.aziendaagricolavendrano.it</footer>
</section>

<section class="sheet sheet-back">
  <article class="wine wine-moscato">
    <div class="wine-label" role="img" aria-label="Etichetta del Moscato d'Asti Cò Ciaro con foglia di vite blu"></div>
    <h2 class="wine-title">Moscato d'Asti DOCG&nbsp; Cò Ciaro</h2>
    <div class="wine-text">
      <p>Il moscato d'Asti DOCG Cò Ciaro dell'Azienda Agricola Vendrano viene prodotto sulla collina di Borgo Alto in Località Vendrano.<br>
      Le uve provengono esclusivamente dalle viti coltivate nei soliti "sori", termine locale che indica "soleggiato" esposto al sole. I sori sono le zone della collina a maggior pendenza le nostre addirittura del 50%, con la migliore esposizione al sole, a Sud-Ovest, a circa 300 metri slm. Il terreno dei sori è marnoso, prevalentemente calcareo, ricco di fossili marini, da cui il colore tendente al bianco. Il microclima è ideale, con una buona escursione termica e una giusta ventilazione che esalta i profumi e i sapori dell'uva.<br>
      Già gli antichi Romani definivano con la parola "LOCUS" un luogo prediletto per coltivare la vite, in poche parole Terreno Ideale meglio noto come "TERROIR".<br>
      La vendemmia, secondo il disciplinare, avviene normalmente tra la fine di agosto e i primi quindici giorni di settembre rigorosamente a mano.<br>
      Si consiglia di berlo freddo a circa 4/6° C, ottimo per accompagnare i dessert.</p>
    </div>
    <div class="tech">
      <div class="tech-title">Scheda tecnica Vermouth</div>
      <table>
        <tr><td>Tipologia</td><td>Vino bianco dolce aromatizzato</td></tr>
        <tr><td>Regione</td><td>Piemonte</td></tr>
        <tr><td>Denominazione</td><td>Vermouth Cò Ciaro</td></tr>
        <tr><td>Annata</td><td>2015</td></tr>
        <tr><td>Formato</td><td>75cl</td></tr>
        <tr><td>Descrizione</td><td>Vermouth di Moscato d'Asti</td></tr>
        <tr><td>Sistema d'allevamento</td><td>Guyot</td></tr>
        <tr><td>Clima</td><td>Altitudine vigneti circa 300 m s.l.m. Esposizione sud-ovest.</td></tr>
        <tr><td>Abbinamento</td><td>Classico aperitivo, ingrediente per cocktail e dolci al cucchiaio</td></tr>
        <tr><td></td><td>16 % vol.</td></tr>
        <tr><td>Grado alcolico</td><td>4,87 g/l</td></tr>
        <tr><td>Acidità totale</td><td>0,40 g/l</td></tr>
        <tr><td>Acidità volatile</td><td>140,2 g/l</td></tr>
        <tr><td>Zuccheri totali</td><td></td></tr>
      </table>
    </div>
  </article>

  <article class="wine wine-vermouth">
    <div class="wine-label" role="img" aria-label="Etichetta del Vermouth Cò Ciaro con foglia di vite grigia"></div>
    <h2 class="wine-title">Vermouth Bianco Cò Ciaro</h2>
    <div class="wine-text">
      <p>Il Vermouth Bianco Cò Ciaro dell'Azienda Agricola Vendrano nasce dalle uve Moscato d'Asti DOCG coltivate sulla collina di Borgo Alto in Località Vendrano.<br>
      Per diventare Vermouth Cò Ciaro il Moscato DOCG è stato arricchito dall'antica ricetta Vermouth Piemonte tramandata da generazioni nella nostra famiglia.<br>
      Classico aperitivo, va servito freddo a circa 3° C con due cubetti di ghiaccio e una scorza di limone.<br>
      Componente indispensabile in fantasiosi Cocktails.</p>
    </div>
    <div class="tech">
      <div class="tech-title">Scheda tecnica Moscato d'Asti DOCG</div>
      <table>
        <tr><td>Tipologia</td><td>Vino bianco dolce</td></tr>
        <tr><td>Regione</td><td>Piemonte</td></tr>
        <tr><td>Denominazione</td><td>Moscato d'Asti DOCG</td></tr>
        <tr><td>Annata</td><td>2015</td></tr>
        <tr><td>Formato</td><td>75cl</td></tr>
        <tr><td>Descrizione</td><td>Moscato d'Asti DOCG</td></tr>
        <tr><td>Sistema d'allevamento</td><td>Guyot</td></tr>
        <tr><td>Clima</td><td>Altitudine vigneti circa 300 m s.l.m. Esposizione sud-ovest.</td></tr>
        <tr><td>Abbinamento</td><td>Dessert, frutta secca, zabaione, formaggi erborinati</td></tr>
        <tr><td>Grado alcolico</td><td>5,5 % vol.</td></tr>
        <tr><td>Acidità totale</td><td>4,88 g/l</td></tr>
        <tr><td>Acidità volatile</td><td>0,24 g/l</td></tr>
        <tr><td>Anidride carbonica</td><td>0,85 atm</td></tr>
        <tr><td>Zuccheri totali</td><td>129,0 g/l</td></tr>
      </table>
    </div>
  </article>

  <div class="back-footer">
    <div class="footer-brand">
      <span class="brand-name">Vendrano</span>
      <span class="brand-sub">Azienda Agricola</span>
    </div>
    <address class="contact" style="font-style:normal">
      <strong>Azienda Agricola Vendrano</strong><br>
      Località Vendrano, 14 12050 Borgo Alto CN Italia<br>
      Partita IVA: 04182260317<br>
      Web: www.aziendaagricolavendrano.it<br>
      Contatto: info@vendrano.it<br>
      Telefono: 0141/552018 – 02/48817305 • Mobile: 347/2291460 – 339/8154072
    </address>
  </div>
  <footer class="web-band">www.aziendaagricolavendrano.it</footer>
</section>

</body>
</html>
```